Biz Card for Harrowfield Property Partners - HWPP

Harrowfield Property Partners is a commercial real estate acquisitions firm. We buy commercial property and need to raise capital from investors for each deal we buy. The vibe needs to be: give us your money, we will multiply it.
Our website: www.hrwpp-example.com
Competitors are: https://velmarholdings-example.com/, https://tribanquepartners-example.com/, http://www.ostrellecapital-example.com/
Target Market(s)
High Net Worth Individuals, Bankers, Insurance Companies, Commercial Real Estate Brokers.
Industry/Entity Type
Investment Banking
Contact Information for Business Card
Name, Title, Addess, Cell#, Office#, email, website
Requirements
Must have
- use one of our logos. See website for look and feel: www.hrwpp-example.com
Nice to have
- see website: www.hrwpp-example.com

```html
<!DOCTYPE html>
<html lang="en">
<head>
<meta charset="UTF-8">
<title>Harrowfield Property Partners – Business Card</title>
<link href="https://fonts.googleapis.com/css2?family=Lato:wght@300;400&family=Arimo:wght@400;700&display=swap" rel="stylesheet">
<style>
  :root {
    --stage: #161616;
    --card: #2a2a2b;
    --silver: #b9b9bb;
    --silver-light: #d6d6d8;
    --ink-white: #f2f2f2;
    --rule: #9a9a9c;
  }
  * { margin: 0; padding: 0; box-sizing: border-box; }
  html, body {
    width: 1200px; height: 900px; overflow: hidden;
    background: var(--stage);
  }
  .canvas {
    position: relative; width: 1200px; height: 900px;
    display: flex; flex-direction: column; align-items: center;
    justify-content: center; gap: 46px;
  }
  .card {
    position: relative; width: 660px; height: 377px;
    background: var(--card);
    box-shadow: 0 8px 24px rgba(0,0,0,0.5);
  }

  /* Wordmark */
  .wordmark {
    font-family: "Lato", sans-serif; font-weight: 300;
    color: var(--silver-light); text-transform: uppercase;
  }
  .wordmark__main { display: block; font-size: 44px; letter-spacing: 7px; line-height: 1; }
  .wordmark__sub { display: block; font-size: 17px; letter-spacing: 6.5px; margin-top: 10px; }
  .mark-circle { position: absolute; border-radius: 50%; background: var(--silver); }

  /* Front */
  .card--front .mark-circle { left: 62px; top: 124px; width: 128px; height: 128px; }
  .card--front .wordmark { position: absolute; left: 214px; top: 150px; }

  /* Back */
  .card--back .mark-circle { left: 125px; top: 66px; width: 120px; height: 120px; }
  .card--back .wordmark { position: absolute; left: 34px; top: 204px; }
  .card--back .wordmark__main { font-size: 33px; letter-spacing: 3.5px; }
  .card--back .wordmark__sub { font-size: 15.5px; letter-spacing: 3.3px; margin-top: 9px; }
  .divider {
    position: absolute; left: 392px; top: 64px; width: 1.5px; height: 252px;
    background: var(--rule);
  }
  .contact {
    position: absolute; left: 418px; top: 68px; right: 20px;
    font-family: "Arimo", sans-serif; color: var(--ink-white);
  }
  .contact__name { font-size: 22px; font-weight: 700; line-height: 1.05; }
  .contact__title { font-size: 16px; color: var(--silver-light); margin-top: 2px; }
  .contact__address { font-size: 14.5px; line-height: 1.3; margin-top: 24px; }
  .contact__list { list-style: none; margin-top: 20px; font-size: 14.5px; }
  .contact__list li { display: flex; align-items: center; gap: 12px; height: 25px; }
  .contact__list svg { width: 16px; height: 16px; flex: none; }
  .contact__web { letter-spacing: 1.5px; }
</style>
</head>
<body>
<main class="canvas">

  <section class="card card--front" aria-label="Business card front">
    <div class="mark-circle"></div>
    <div class="wordmark">
      <span class="wordmark__main">Harrowfield</span>
      <span class="wordmark__sub">Property Partners</span>
    </div>
  </section>

  <section class="card card--back" aria-label="Business card back">
    <div class="mark-circle"></div>
    <div class="wordmark">
      <span class="wordmark__main">Harrowfield</span>
      <span class="wordmark__sub">Property Partners</span>
    </div>
    <div class="divider"></div>
    <div class="contact">
      <p class="contact__name">Marcus Everly</p>
      <p class="contact__title">President</p>
      <p class="contact__address">418 Linden Crest Ave, Suite 900<br>Harbor Point, FL 33001</p>
      <ul class="contact__list">
        <li>
          <svg viewBox="0 0 16 16" fill="none" stroke="#f2f2f2" stroke-width="1.3"><rect x="4" y="1" width="8" height="14" rx="1.5"/><line x1="7" y1="12.5" x2="9" y2="12.5"/></svg>
          <span>(555) 013-2748</span>
        </li>
        <li>
          <svg viewBox="0 0 16 16" fill="#f2f2f2"><path d="M1 6c0-2 3-3.5 7-3.5S15 4 15 6l-3 1-1-2H5L4 7z"/><rect x="3" y="8" width="10" height="6" rx="1"/></svg>
          <span>(555) 013-0000</span>
        </li>
        <li>
          <svg viewBox="0 0 16 16" fill="none" stroke="#f2f2f2" stroke-width="1.3"><rect x="1" y="3.5" width="14" height="9"/><polyline points="1,3.5 8,9 15,3.5"/></svg>
          <span>info@hrwpp-example.com</span>
        </li>
        <li>
          <svg viewBox="0 0 16 16" fill="none" stroke="#f2f2f2" stroke-width="1.2"><circle cx="8" cy="8" r="6.5"/><ellipse cx="8" cy="8" rx="3" ry="6.5"/><line x1="1.5" y1="8" x2="14.5" y2="8"/><line x1="2.5" y1="4.8" x2="13.5" y2="4.8"/><line x1="2.5" y1="11.2" x2="13.5" y2="11.2"/></svg>
          <span class="contact__web">www.hrwpp-example.com</span>
        </li>
      </ul>
    </div>
  </section>

</main>
</body>
</html>
```